New Company Business Card Design

I have a new company logo and I want a new business card design. I dont know if the logo file i attached is in the correct format or quality. We are a New York City Specialty construction Firm specializing in high risk out of the box projects. I want a simple and classy business card that people will his card is as crisp as the work his company does.

Target Market(s)

Clients in the heavy construction industry in New York City

Industry/Entity Type

Construction Company

Contact Information for Business Card

Simple Classy - DIFFERENT

Font styles to use
Other font styles liked:
• Mach the logo font in some way

Colors

Designer to choose colors to be used in the design.

Requirements
Must have
• Uniqueness
Nice to have
• Nothing particular - Just different and classy - Timeless
Should not have
• Goofy Shit or Gimmicky shit

```html
<!DOCTYPE html>
<html lang="en">
<head>
<meta charset="utf-8">
<title>Korvane Builders – Business Card</title>
<link href="https://fonts.googleapis.com/css2?family=Roboto:wght@400;700;900&display=swap" rel="stylesheet">
<style>
  :root {
    --page: #ffffff;
    --brand-blue: #0a84c9;
    --brand-blue-deep: #0b5fa8;
    --ink: #0d0d0d;
    --paper: #ffffff;
    --city-light: #eeeeee;
    --city-mid: #c9c9c9;
    --city-dark: #9a9a9a;
  }
  * { box-sizing: border-box; margin: 0; padding: 0; }
  html, body {
    width: 800px; height: 1200px; overflow: hidden;
    background: var(--page);
    font-family: "Roboto", Arial, sans-serif;
  }
  .sheet { position: relative; width: 800px; height: 1200px; }

  .card {
    position: absolute; left: 56px; width: 688px; height: 392px;
    background: var(--paper); overflow: hidden;
  }
  .card--front { top: 130px; }
  .card--back { top: 674px; }

  /* front */
  .front-skyline {
    position: absolute; inset: 0;
    background: linear-gradient(180deg, var(--city-light) 0%, var(--city-mid) 45%, #b5b5b5 100%);
  }
  .front-wordmark {
    position: absolute; left: 96px; top: 110px; width: 492px;
    text-align: center;
    font-weight: 900; font-size: 44px; line-height: 1.15; letter-spacing: 3px;
    color: var(--brand-blue-deep);
  }
  .web-bar {
    position: absolute; left: 92px; top: 360px; width: 488px; height: 32px;
    background: var(--ink); border-radius: 4px 4px 0 0;
    color: #fff; font-weight: 700; font-size: 21px;
    display: flex; align-items: center; justify-content: center;
  }
  .web-tab {
    position: absolute; top: 374px; width: 79px; height: 18px;
    background: var(--brand-blue); border-radius: 4px 4px 0 0;
  }
  .web-tab--left { left: 52px; }
  .web-tab--right { left: 541px; }

  /* back */
  .back-skyline {
    position: absolute; left: 0; top: 0; width: 400px; height: 392px;
    background: linear-gradient(90deg, var(--city-mid) 0%, var(--city-light) 55%, rgba(255,255,255,0) 100%);
    opacity: 0.85;
  }
  .back-wordmark {
    position: absolute; left: 396px; top: 48px; width: 250px;
    text-align: center;
    font-weight: 900; font-size: 26px; line-height: 1.15; letter-spacing: 2px;
    color: var(--brand-blue-deep);
  }
  .portrait {
    position: absolute; left: 186px; top: 99px; width: 100px; height: 100px;
    border-radius: 50%; border: 4px solid var(--brand-blue);
    background: linear-gradient(160deg, #c9d3dc 0%, #8b97a3 100%);
  }
  .name-plate {
    position: absolute; left: 128px; top: 206px; width: 216px; height: 66px;
    background: var(--ink); border-radius: 6px 0 0 6px;
    text-align: center; padding-top: 11px;
  }
  .name-plate__name { color: #fff; font-size: 20px; font-weight: 400; }
  .name-plate__role { color: var(--brand-blue); font-size: 12px; font-weight: 700; letter-spacing: 0.5px; margin-top: 3px; }

  .contact-panel {
    position: absolute; left: 344px; top: 150px; width: 346px; height: 242px;
    background: var(--brand-blue); border-radius: 20px 0 0 0;
  }
  .contact-row { position: absolute; left: 0; width: 346px; height: 50px; }
  .contact-row__text {
    position: absolute; left: 0; width: 264px; top: 0;
    text-align: center; color: #fff; font-size: 16px; line-height: 20px;
  }
  .contact-row__icon {
    position: absolute; left: 256px; top: 3px; width: 44px; height: 44px;
  }
  .contact-row--phone { top: 30px; }
  .contact-row--web { top: 92px; }
  .contact-row--place { top: 168px; }
</style>
</head>
<body>
<div class="sheet">

  <section class="card card--front">
    <div class="front-skyline" role="img" aria-label="Black and white aerial view of the New York City skyline"></div>
    <div class="front-wordmark">KORVANE<br>BUILDERS, INC.</div>
    <div class="web-tab web-tab--left"></div>
    <div class="web-tab web-tab--right"></div>
    <div class="web-bar">www.korvanebuild.com</div>
  </section>

  <section class="card card--back">
    <div class="back-skyline" role="img" aria-label="Faded black and white city skyscrapers"></div>
    <div class="back-wordmark">KORVANE<br>BUILDERS, INC.</div>
    <div class="portrait" role="img" aria-label="Portrait photo of the card holder"></div>
    <div class="name-plate">
      <div class="name-plate__name">Dana Whitlock</div>
      <div class="name-plate__role">ENGINEER</div>
    </div>

    <div class="contact-panel">
      <div class="contact-row contact-row--phone">
        <p class="contact-row__text">+00412557801<br>+00412557846</p>
        <svg class="contact-row__icon" viewBox="0 0 44 44" aria-hidden="true">
          <circle cx="22" cy="22" r="22" fill="#0d0d0d"/>
          <path d="M15 12c1-1 2.5-1 3.3 0l2.4 3c.7.9.6 2-.2 2.8l-1.4 1.3c1 2.3 2.9 4.3 5.3 5.4l1.3-1.4c.8-.8 2-.9 2.8-.2l3 2.4c1 .8 1 2.3 0 3.3l-1.6 1.6c-1.5 1.5-4 1.7-6.6.3-4.5-2.4-8-6-10.3-10.4-1.4-2.6-1.2-5.1.3-6.6z" fill="#fff"/>
        </svg>
      </div>
      <div class="contact-row contact-row--web">
        <p class="contact-row__text">dana.whitlock@korvanebuild.com<br>www.korvanebuild.com</p>
        <svg class="contact-row__icon" viewBox="0 0 44 44" aria-hidden="true">
          <circle cx="22" cy="22" r="22" fill="#0d0d0d"/>
          <g fill="none" stroke="#fff" stroke-width="1.6">
            <circle cx="22" cy="22" r="11"/>
            <ellipse cx="22" cy="22" rx="5" ry="11"/>
            <line x1="11" y1="22" x2="33" y2="22"/>
            <path d="M13 16.5h18M13 27.5h18"/>
          </g>
        </svg>
      </div>
      <div class="contact-row contact-row--place">
        <p class="contact-row__text">48, Harbor Lane<br>New York, USA 10017</p>
        <svg class="contact-row__icon" viewBox="0 0 44 44" aria-hidden="true">
          <circle cx="22" cy="22" r="22" fill="#0d0d0d"/>
          <path d="M22 10c-4.7 0-8.5 3.7-8.5 8.4 0 6.3 8.5 15.6 8.5 15.6s8.5-9.3 8.5-15.6C30.5 13.7 26.7 10 22 10z" fill="#fff"/>
          <circle cx="22" cy="18.5" r="3.2" fill="#0d0d0d"/>
        </svg>
      </div>
    </div>
  </section>

</div>
</body>
</html>
```